Gift Card Design - Suds Harbor Co

I am needing a design for a standard plastic gift card, (ever so slightly large then a standard rounded edge business card). Name of the business is Suds Harbor Co. Attached is a file with a poor example, done by an equipment manufacturing firm, that I feel could be much better. Simple, clean and classy with what it is and does along with our name is what I am looking for. Attached also is out logo and source of logo, they don't have to be on the card.

Target Market(s)

Car wash customers in an upscale market.

Industry/Entity Type

Business

Font styles to use
Serif
Other font styles liked:
• whatever you feel, but I do like the font on a Brevanto golf ball

Requirements
Must have
• Words anywhere on the card -
• Reloadable Card
• Self Serve Bays & Vacuums.
• Also need name of the business, Suds Harbor Co.
Nice to have
• Work in Pantone #7483 as there is existing signage with that as a primary color, just trying to tie things together. Attached is my business logo and a picture of the source of the logo, you do not have to use those if you don't want to. I do like clean and classy but am open to creativity, that's why I am submitting this project.
Should not have
• Naked lady pictures

```html
<!DOCTYPE html>
<html lang="en">
<head>
<meta charset="utf-8">
<title>Suds Harbor Co — Reloadable Card</title>
<link href="https://fonts.googleapis.com/css2?family=Montserrat:wght@300;700&display=swap" rel="stylesheet">
<style>
  :root {
    --backdrop: #e3e4e4;
    --card-green: #1b4a26;
    --card-deep: #0b160e;
    --card-black: #050605;
    --accent-yellow: #ecea12;
    --text-white: #ffffff;
    --text-soft: #d9dcd9;
    --foam-light: #5e625f;
    --foam-dark: #141514;
  }
  html, body {
    margin: 0;
    padding: 0;
    width: 1200px;
    height: 1000px;
    overflow: hidden;
    background: var(--backdrop);
  }
  .canvas {
    position: relative;
    width: 1200px;
    height: 1000px;
  }
  .gift-card {
    position: absolute;
    left: 120px;
    top: 161px;
    width: 960px;
    height: 678px;
    border-radius: 28px;
    overflow: hidden;
    box-shadow: 0 8px 24px rgba(0,0,0,0.18);
  }
  .gift-card svg {
    display: block;
    width: 100%;
    height: 100%;
  }
  .brand-name {
    font-family: "Montserrat", sans-serif;
    font-weight: 700;
    font-size: 44px;
    fill: var(--text-white);
  }
  .card-label {
    font-family: "Montserrat", sans-serif;
    font-weight: 300;
    font-size: 17px;
    letter-spacing: 8px;
    fill: var(--text-soft);
  }
  .service-line {
    font-family: "Montserrat", sans-serif;
    font-weight: 700;
    font-size: 15px;
    fill: var(--text-white);
  }
</style>
</head>
<body>
<main class="canvas">
  <div class="gift-card">
    <svg viewBox="0 0 607 429" xmlns="http://www.w3.org/2000/svg">
      <defs>
        <linearGradient id="card-fill" x1="0" y1="0" x2="0" y2="1">
          <stop offset="0" stop-color="var(--card-green)"/>
          <stop offset="0.45" stop-color="var(--card-deep)"/>
          <stop offset="1" stop-color="var(--card-black)"/>
        </linearGradient>
        <linearGradient id="foam-fill" x1="0" y1="0" x2="0" y2="1">
          <stop offset="0" stop-color="var(--foam-light)" stop-opacity="0"/>
          <stop offset="0.55" stop-color="var(--foam-light)" stop-opacity="0.4"/>
          <stop offset="1" stop-color="var(--foam-dark)" stop-opacity="0.6"/>
        </linearGradient>
      </defs>

      <rect class="card-base" width="607" height="429" fill="url(#card-fill)"/>
      <rect class="foam-photo" role="img" aria-label="Close-up photo of soap suds and foam bubbles"
            x="0" y="240" width="607" height="189" fill="url(#foam-fill)"/>

      <text class="brand-name" x="303.5" y="180" text-anchor="middle">Suds Harbor Co</text>
      <text class="card-label" x="307.5" y="226" text-anchor="middle">RELOADABLE CARD</text>

      <polygon class="accent-stripe" points="520,429 607,322 607,392 577,429" fill="var(--accent-yellow)"/>

      <g class="service-list" text-anchor="end">
        <text class="service-line" x="570" y="342">SELF</text>
        <text class="service-line" x="570" y="357">SERVE</text>
        <text class="service-line" x="570" y="372">BAYS &amp;</text>
        <text class="service-line" x="570" y="387">VACUUMS</text>
      </g>
    </svg>
  </div>
</main>
</body>
</html>
```